Congressional Website with splash page for Texas Democratic Black Woman

I would like a splash page with a turquoise shaded theme to it. My logo can be played with but the original logo is black white and red... we are now wanting a page that is in shades of turquoise with the black white and red colors. On the splash page, I want to collect volunteer information and prompt people to donate. I would like to.just have a large picture of me of some sort and then you have to click to enter the rest of the page with the issues.

Target Market(s)

Voters and Donors and democrats

Industry/Entity Type

campaign/elections

Coding

Coded - Design and coding required

Number of Pages Required

2 page

Font styles to use
Serif

Colors
0094D4
00A9DD
6FCCEA
C7EBF8
E9F6FB

Requirements
Must have
• I must have a landing page... and then it open up to the other pages.

```html
<!DOCTYPE html>
<html lang="en">
<head>
<meta charset="utf-8">
<title>Marisol Whitfield for Congress</title>
<link rel="stylesheet" href="https://fonts.googleapis.com/css2?family=Playfair+Display:wght@400;700&family=Great+Vibes&family=Oswald:wght@500;600&family=Figtree:wght@400;500&display=swap">
<style>
  :root {
    --teal-deep: #17bfa8;
    --teal: #2fd1bf;
    --teal-light: #5fe3d3;
    --red: #f5081f;
    --white: #ffffff;
    --ink: #111111;
    --text: #222222;
    --muted: #7a7a7a;
    --footer: #1b1b1b;
  }
  * { box-sizing: border-box; margin: 0; padding: 0; }
  html, body { width: 684px; height: 1200px; overflow: hidden; background: var(--white); }
  .page { position: relative; width: 684px; height: 1200px; overflow: hidden; font-family: "Figtree", sans-serif; color: var(--text); }

  /* Hero */
  .hero { position: absolute; left: 0; top: 0; width: 684px; height: 450px;
    background: linear-gradient(100deg, var(--teal-deep) 0%, var(--teal) 45%, var(--teal-light) 100%); }
  .hero-city { position: absolute; left: 0; top: 180px; width: 684px; height: 260px;
    background: linear-gradient(180deg, rgba(20,150,135,0) 0%, rgba(20,150,135,0.28) 60%, rgba(20,150,135,0.18) 100%); }
  .hero-curve { position: absolute; left: 0; top: 370px; }

  .brand { position: absolute; left: 66px; top: 30px; display: flex; align-items: center; gap: 7px; }
  .brand-mark { width: 10px; height: 10px; border-radius: 50%; background: var(--white); }
  .brand-name { font-family: "Figtree", sans-serif; font-weight: 500; font-size: 15px; color: var(--white); letter-spacing: 0.3px; }

  .welcome { position: absolute; left: 68px; top: 135px; font-family: "Oswald", sans-serif; font-weight: 600; font-size: 14px; letter-spacing: 3px; color: var(--white); }
  .hero-first { position: absolute; left: 64px; top: 152px; font-family: "Playfair Display", serif; font-size: 56px; line-height: 1; color: var(--white); letter-spacing: -0.5px; }
  .hero-last { position: absolute; left: 60px; top: 204px; font-family: "Great Vibes", cursive; font-size: 58px; line-height: 1; color: var(--white); }

  .btn-frame { position: absolute; left: 74px; top: 286px; width: 129px; height: 31px; border: 1px solid var(--white); }
  .btn-enter { position: absolute; left: 69px; top: 281px; width: 129px; height: 32px; background: var(--red); color: var(--white);
    font-family: "Oswald", sans-serif; font-weight: 600; font-size: 12px; letter-spacing: 2.5px; display: flex; align-items: center; justify-content: center; }

  .photo-frame { position: absolute; left: 327px; top: 70px; width: 164px; height: 172px; border: 1.5px solid var(--white); border-right: none; }
  .photo-frame::after { content: ""; position: absolute; right: 0; top: -1.5px; width: 1.5px; height: 14px; background: var(--white); }
  .hero-photo { position: absolute; left: 339px; top: 85px; width: 304px; height: 257px; border-radius: 0 40px 0 40px;
    background: linear-gradient(160deg, #c9a25a 0%, #d9a62e 40%, #a86f1c 75%, #7a5122 100%); }

  /* Issues */
  .portrait-ring { position: absolute; left: 67px; top: 477px; width: 244px; height: 244px; border-radius: 50%; border: 1.5px solid var(--teal); }
  .portrait { position: absolute; left: 74px; top: 484px; width: 230px; height: 230px; border-radius: 50%;
    background: radial-gradient(circle at 50% 45%, #e8ddd2 0%, #c9b39b 45%, #7a4a2c 100%); }

  .issues-title { position: absolute; left: 340px; top: 475px; font-family: "Figtree", sans-serif; font-weight: 500; font-size: 25px; color: var(--ink); letter-spacing: 0.3px; }
  .rule-red { position: absolute; height: 2px; background: var(--red); }
  .issues-rule { left: 344px; top: 506px; width: 45px; }
  .issue-list { position: absolute; list-style: none; }
  .issue-list li { position: relative; height: 32.5px; padding-left: 30px; font-size: 11px; line-height: 20px; color: var(--text); }
  .issue-list svg { position: absolute; left: 0; top: 1px; width: 19px; height: 19px; fill: none; stroke: var(--red); stroke-width: 1.3; }
  .issues-left { left: 341px; top: 533px; }
  .issues-right { left: 499px; top: 535px; }

  .learn-frame { position: absolute; left: 346px; top: 680px; width: 98px; height: 26px; border: 1px solid var(--teal); }
  .btn-learn { position: absolute; left: 343px; top: 677px; width: 97px; height: 26px; background: var(--teal); color: var(--white);
    font-family: "Oswald", sans-serif; font-weight: 600; font-size: 10px; letter-spacing: 2px; display: flex; align-items: center; justify-content: center; }

  /* Volunteer */
  .volunteer { position: absolute; left: 0; top: 778px; width: 684px; height: 328px;
    background: linear-gradient(100deg, var(--teal-deep) 0%, var(--teal) 45%, var(--teal-light) 100%); }
  .volunteer-city { position: absolute; left: 0; top: 200px; width: 684px; height: 128px;
    background: linear-gradient(180deg, rgba(20,150,135,0) 0%, rgba(20,150,135,0.22) 100%); }
  .drop { position: absolute; left: 339px; top: 32px; }
  .eyebrow { position: absolute; left: 0; top: 48px; width: 684px; text-align: center; font-family: "Oswald", sans-serif; font-weight: 600; font-size: 11px; letter-spacing: 2.5px; color: var(--white); }
  .volunteer-title { position: absolute; left: 0; top: 63px; width: 684px; text-align: center; font-weight: 400; font-size: 24px; color: var(--white); letter-spacing: 0.2px; }
  .volunteer-rule { left: 327px; top: 96px; width: 41px; }
  .field { position: absolute; background: var(--white); border: 1px solid #d6d6d6; font-size: 8px; color: var(--muted); padding-left: 12px; display: flex; align-items: center; }
  .field-name { left: 107px; top: 113px; width: 237px; height: 30px; }
  .field-email { left: 107px; top: 149px; width: 237px; height: 30px; }
  .field-phone { left: 107px; top: 186px; width: 237px; height: 30px; }
  .field-message { left: 351px; top: 113px; width: 237px; height: 103px; align-items: flex-start; padding-top: 10px; }
  .btn-submit { position: absolute; left: 283px; top: 232px; width: 130px; height: 30px; border-radius: 15px; background: var(--red); color: var(--white);
    font-family: "Oswald", sans-serif; font-weight: 600; font-size: 13px; letter-spacing: 2.5px; display: flex; align-items: center; justify-content: center; }

  /* Footer */
  .footer { position: absolute; left: 0; top: 1106px; width: 684px; height: 94px; background: var(--footer); }
  .copyright { position: absolute; left: 0; top: 21px; width: 684px; text-align: center; font-size: 8px; color: var(--white); }
  .social { position: absolute; left: 306px; top: 40px; display: flex; gap: 4px; }
  .social span { width: 18px; height: 18px; border-radius: 50%; background: var(--white); }
</style>
</head>
<body>
<div class="page">

  <header class="hero">
    <div class="hero-city" role="img" aria-label="Faded aerial view of a downtown skyline"></div>

    <div class="brand">
      <span class="brand-mark"></span>
      <span class="brand-name">Marisol Whitfield</span>
    </div>

    <div class="welcome">WELCOME TO</div>
    <div class="hero-first">MARISOL</div>
    <div class="hero-last">Whitfield</div>

    <div class="btn-frame"></div>
    <a class="btn-enter">CLICK TO ENTER</a>

    <div class="photo-frame"></div>
    <div class="hero-photo" role="img" aria-label="Portrait of the candidate seated on a wooden bench in a capitol hallway"></div>

    <svg class="hero-curve" width="684" height="80" viewBox="0 0 684 80">
      <path d="M0 75 Q342 -10 684 75 L684 80 L0 80 Z" fill="#ffffff"/>
      <path d="M100 52 Q342 18 590 52" fill="none" stroke="#f5081f" stroke-width="2.5"/>
    </svg>
  </header>

  <section class="issues">
    <div class="portrait-ring"></div>
    <div class="portrait" role="img" aria-label="Portrait of the candidate in a white blazer seated at a desk"></div>

    <h2 class="issues-title">OUR ISSUES</h2>
    <div class="rule-red issues-rule"></div>

    <ul class="issue-list issues-left">
      <li><svg viewBox="0 0 20 20"><rect x="2" y="9" width="16" height="9"/><line x1="2" y1="13" x2="18" y2="13"/><path d="M6 9 L10 3 L14 7 L12 9"/></svg>Voting Rights</li>
      <li><svg viewBox="0 0 20 20"><path d="M10 17 L3 10 A4 4 0 0 1 10 5 A4 4 0 0 1 17 10 Z"/><polyline points="2,11 7,11 9,8 11,14 13,11 18,11"/></svg>Healthcare</li>
      <li><svg viewBox="0 0 20 20"><circle cx="10" cy="4" r="2"/><path d="M3 9 L6 17 L9 17 M17 9 L14 17 L11 17"/></svg>Worker’s Rights</li>
      <li><svg viewBox="0 0 20 20"><line x1="10" y1="2" x2="10" y2="18"/><line x1="3" y1="6" x2="17" y2="6"/><path d="M1 12 L4 6 L7 12 Z M13 12 L16 6 L19 12 Z"/><line x1="6" y1="18" x2="14" y2="18"/></svg>Reproductive Justice</li>
    </ul>

    <ul class="issue-list issues-right">
      <li><svg viewBox="0 0 20 20"><circle cx="10" cy="8" r="6"/><line x1="4" y1="8" x2="16" y2="8"/><ellipse cx="10" cy="8" rx="2.5" ry="6"/><line x1="3" y1="17" x2="17" y2="17"/></svg>Immigration</li>
      <li><svg viewBox="0 0 20 20"><circle cx="6" cy="14" r="3.5"/><circle cx="14" cy="6" r="3.5"/><line x1="8.5" y1="11.5" x2="11.5" y2="8.5"/></svg>Criminal Justice</li>
      <li><svg viewBox="0 0 20 20"><circle cx="10" cy="10" r="8"/><circle cx="10" cy="10" r="4.5"/><line x1="10" y1="7" x2="10" y2="13"/></svg>Economy</li>
      <li><svg viewBox="0 0 20 20"><path d="M1 8 L10 4 L19 8 L10 12 Z"/><path d="M5 10 L5 14 Q10 17 15 14 L15 10"/><line x1="17" y1="9" x2="17" y2="15"/></svg>Education</li>
    </ul>

    <div class="learn-frame"></div>
    <a class="btn-learn">LEARN MORE</a>
  </section>

  <section class="volunteer">
    <div class="volunteer-city" role="img" aria-label="Faded city skyline silhouette"></div>
    <svg class="drop" width="12" height="14" viewBox="0 0 12 14"><path d="M6 0 Q12 7 10 10.5 A4.5 4.5 0 0 1 2 10.5 Q0 7 6 0 Z" fill="#f5081f"/></svg>
    <div class="eyebrow">WANT TO DONATE</div>
    <h2 class="volunteer-title">VOLUNTEER FORM</h2>
    <div class="rule-red volunteer-rule"></div>

    <div class="field field-name">Your Name*</div>
    <div class="field field-email">E-mail address*</div>
    <div class="field field-phone">Phone</div>
    <div class="field field-message">Message</div>
    <a class="btn-submit">SUBMIT</a>
  </section>

  <footer class="footer">
    <p class="copyright">© 2021 Marisol Whitfield | All Rights Reserved</p>
    <div class="social"><span></span><span></span><span></span><span></span></div>
  </footer>

</div>
</body>
</html>
```